Größen anpassen für versch. Werbemittel
Zielgruppe
Wir organisieren Messen rund um die Frau!
Aufgabenstellung
Das Layout steht soweit und müsste nur angepasst werden.
Wir benötigen folgendes:
Das beigefügte Plakat in folgenden Größen:
a1 - sollen bei Papierfalke gedruclt werden!
a3 - II
2m² Traffic Bord 120x75 ohne Beschnitt-Hochformat-Schriften vektorisieren!
Berliner Rahmen: Plakatdruck 2/1-(A0)-Querformat 84,1 x 118,5 cm, 115 g Affichenpapier 4-farbirg Euroskala
Großflächen: S. Anlage
LED Tafeln:
Immer der Fotocredit Brigitte Solweck dazu! Wichtig!
Das Logo aber sollte oben hin, dann das Foto, darunter der Text.
Irgendwo sollte noch dazu:
Die Trend- und Eventmesse rund um die Frau (oder ähnlich),
damit man direkt weiß, um was es geht ;)

```html
<!DOCTYPE html>
<html lang="de">
<head>
<meta charset="utf-8">
<title>LUMINA – Trend- &amp; Eventmesse rund um die Frau</title>
<link rel="stylesheet" href="https://fonts.googleapis.com/css2?family=Kalam:wght@700&family=Open+Sans:wght@300;400;700&display=swap">
<style>
  :root {
    --magenta: #c31a6b;
    --ink: #1d1d1b;
    --grey: #555555;
    --rule: #8a8a8a;
    --blossom: #ecc3db;
    --paper: #ffffff;
  }
  * { margin: 0; padding: 0; box-sizing: border-box; }
  html, body { width: 1200px; height: 849px; overflow: hidden; background: var(--paper); }
  .poster {
    position: relative;
    width: 1200px;
    height: 849px;
    overflow: hidden;
    background: var(--paper);
    font-family: "Open Sans", Arial, sans-serif;
  }
  .brand {
    position: absolute;
    left: 50px;
    top: 12px;
    width: 506px;
    text-align: center;
  }
  .brand-name {
    font-family: "Open Sans", Arial, sans-serif;
    font-weight: 300;
    font-size: 128px;
    line-height: 1.1;
    letter-spacing: 0.04em;
    color: var(--ink);
  }
  .portrait {
    position: absolute;
    left: 0;
    top: 222px;
    width: 600px;
    height: 627px;
    background:
      radial-gradient(ellipse 38% 32% at 47% 40%, #d9a98b 0%, #b78464 45%, rgba(120,85,60,0) 80%),
      radial-gradient(ellipse 55% 40% at 50% 85%, #f3e4df 0%, #ecdcd7 60%, rgba(236,220,215,0) 100%),
      linear-gradient(100deg, #9aa3a6 0%, #d9dee0 22%, #eef1f2 60%, #f6f7f8 100%);
  }
  .photo-credit {
    position: absolute;
    left: 27px;
    top: 813px;
    font-size: 8px;
    color: var(--ink);
  }
  .blossom {
    position: absolute;
    border-radius: 50%;
  }
  .blossom-top {
    left: 560px;
    top: -40px;
    width: 380px;
    height: 330px;
    background: radial-gradient(ellipse at 40% 30%, rgba(236,195,219,0.75) 0%, rgba(236,195,219,0.35) 45%, rgba(236,195,219,0) 72%);
  }
  .blossom-bottom {
    left: 940px;
    top: 500px;
    width: 300px;
    height: 380px;
    background: radial-gradient(ellipse at 70% 70%, rgba(236,195,219,0.75) 0%, rgba(236,195,219,0.35) 45%, rgba(236,195,219,0) 72%);
  }
  .info {
    position: absolute;
    left: 620px;
    width: 580px;
    text-align: center;
  }
  .headline {
    top: 66px;
    font-family: "Kalam", cursive;
    font-weight: 700;
    font-size: 52px;
    line-height: 53px;
    color: var(--magenta);
  }
  .event-date {
    top: 282px;
    font-weight: 700;
    font-size: 30px;
    line-height: 38px;
    color: var(--grey);
  }
  .slogan {
    top: 534px;
    font-weight: 400;
    font-size: 32px;
    line-height: 39px;
    color: var(--magenta);
    text-transform: uppercase;
  }
  .divider {
    position: absolute;
    left: 678px;
    top: 726px;
    width: 443px;
    height: 1px;
    background: var(--rule);
  }
  .web {
    left: 640px;
    width: 520px;
    top: 748px;
    font-weight: 700;
    font-size: 42px;
    line-height: 52px;
    color: var(--magenta);
  }
</style>
</head>
<body>
<main class="poster">
  <div class="blossom blossom-top" role="img" aria-label="Zarte rosa Blumenranke mit Blüten und Schmetterlingen"></div>
  <div class="blossom blossom-bottom" role="img" aria-label="Zarte rosa Blumenranke mit Blüten"></div>

  <header class="brand">
    <div class="brand-name">LUMINA</div>
  </header>

  <div class="portrait" role="img" aria-label="Porträtfoto einer lächelnden Frau mit schulterlangem braunem Haar und hellem Oberteil"></div>
  <p class="photo-credit">Fotocredit: Brigitte Solweck</p>

  <h1 class="info headline">TREND –<br>&amp; EVENTMESSE<br>rund um die Frau</h1>

  <p class="info event-date">29 &amp; 30 April 2017<br>Kongress Forum Velbach</p>

  <p class="info slogan">Dein Tag zum Wohlfühlen,<br>Schönsein, Lautlachen,<br>Sachenmachen</p>

  <div class="divider"></div>

  <p class="info web">www.lumina-messen.de</p>
</main>
</body>
</html>
```